Scrum Vanguards Rising Captains Initiative Website Design

Task:

A Website Design that has the ability for people to book onto events and Pay.

The design should reflect the colours and brand of the logo and what you have done for the Flyer, Facebook and Twitter pages. The same brand Family. The website needs to be clean and not cluttered.

5 Pages which include:

1. Home
2. Programme
3. Booking
4. FAQs
5. Vanguards

It should clean, easy to read and inviting for children to book onto the programme.

The Website domain will be www.vanguards-rci.example

Happy to use rugby stock pictures children if you need to. Must be Rugby.

Target Market(s)

Children Age 11+ and their Parents

Contact Information for Business Card

One Side the Logo

Other side: Name. Job. Contact No. Email. Rising Captains Initiative

Number of Pages Required

5+ page

Font styles to use
Serif
Sans Serif

Requirements
Must have
• The flyer design attached as a document shows the colours of the brand - this MUST be consistent throughout the 5 Pages
• I must be able to use https://www.tixbrell.example for booking the events online
• The Business Card Files must allow me to change names, roles etc
Should not have
• It should not be cluttered

```html
<!DOCTYPE html>
<html lang="en">
<head>
<meta charset="utf-8">
<title>Rugby Vanguards – Rising Captains Initiative</title>
<link href="https://fonts.googleapis.com/css2?family=Oswald:wght@400;500;600&family=Open+Sans:wght@400;600;700&display=swap" rel="stylesheet">
<style>
:root{
  --gold:#f7b21b;
  --gold-deep:#e3a10f;
  --ink:#1b1b1b;
  --text:#555555;
  --grey-band:#f4f4f4;
  --panel:#f6f6f6;
  --faq-head:#888888;
  --line:#bdbdbd;
  --footer:#0d0d0d;
  --white:#ffffff;
  --head-font:'Oswald',sans-serif;
  --body-font:'Open Sans',sans-serif;
}
*{box-sizing:border-box;margin:0;padding:0}
html,body{width:1200px;height:3462px;overflow:hidden}
body{position:relative;background:var(--white);font-family:var(--body-font);color:var(--text)}
.abs{position:absolute}

/* Hero */
.hero{left:0;top:0;width:1200px;height:632px;background:linear-gradient(180deg,#2a2d27 0%,#3f4a3a 45%,#242821 100%)}
.hero-shade{left:0;top:0;width:1200px;height:632px;background:radial-gradient(ellipse at 55% 55%,rgba(70,110,70,.35),rgba(0,0,0,.25) 70%)}
.brand{left:97px;top:14px;width:150px;text-align:center;color:var(--gold);font-family:var(--head-font)}
.brand-mark{display:block;width:64px;height:64px;margin:0 auto 10px;border-radius:50%;background:var(--gold)}
.brand-name{font-size:22px;font-weight:500;line-height:1.1;letter-spacing:.5px}
.nav{right:95px;top:56px;display:flex;gap:32px;align-items:center;font-family:var(--head-font);font-size:15px;font-weight:500;color:var(--white);letter-spacing:.3px}
.nav .active{color:var(--gold)}
.hero-title{left:0;top:190px;width:1200px;text-align:center;font-family:var(--head-font);font-weight:500;font-size:94px;color:var(--white);letter-spacing:1px;line-height:1.1}
.hero-sub{left:0;top:312px;width:1200px;text-align:center;font-size:25px;line-height:37px;color:var(--white)}
.btn{display:flex;align-items:center;justify-content:center;font-family:var(--body-font);font-weight:600;text-transform:uppercase}
.hero-btn{left:505px;top:422px;width:190px;height:63px;background:var(--gold);color:var(--white);font-size:20px}
.dots{left:566px;top:567px;display:flex;gap:4px}
.dots span{width:16px;height:16px;border-radius:50%;border:2px solid var(--white)}
.dots span.on{background:var(--white)}

/* Welcome */
.welcome-img{left:99px;top:715px;width:508px;height:478px;background:linear-gradient(160deg,#a44a4a 0%,#5d7b4a 55%,#3f7a32 100%)}
.welcome-card{left:549px;top:752px;width:552px;height:404px;background:var(--panel);padding:52px 42px}
.welcome-card h2{font-family:var(--head-font);font-weight:500;font-size:36px;color:var(--ink);letter-spacing:.5px;margin-bottom:26px}
.welcome-card p{font-size:14.5px;line-height:27px;margin-bottom:24px}
.small-btn{width:120px;height:44px;background:var(--gold);color:var(--white);font-size:14px}

/* Programs */
.programs{left:0;top:1290px;width:1200px;height:766px;background:var(--grey-band)}
.section-title{left:0;width:1200px;text-align:center;font-family:var(--head-font);font-weight:500;font-size:36px;color:var(--ink);letter-spacing:.5px}
.tab{top:1433px;height:51px;border:2px solid #9a9a9a;background:var(--white);color:var(--ink);font-size:15px}
.tab.on{border-color:var(--gold);color:var(--gold)}
.card-img{top:1532px;width:319px;height:240px}
.card-title{top:1810px;font-family:var(--head-font);font-size:21px;color:var(--ink)}
.card-date{top:1850px;font-size:13.5px;display:flex;align-items:center;gap:8px}
.card-price{top:1882px;font-weight:700;font-size:21px;color:var(--ink)}
.card-btn{top:1932px;width:134px;height:48px;border:2px solid var(--gold);color:var(--gold);font-size:14px}

/* FAQs */
.faq{left:99px;width:1002px;border:2px solid #cfcfcf;display:flex;align-items:center;font-size:17px;color:var(--ink)}
.faq .sign{width:62px;height:100%;background:var(--faq-head);color:var(--white);display:flex;align-items:center;justify-content:center;font-size:26px;font-weight:700}
.faq .q{padding-left:4px;margin-left:6px}
.faq.open{background:var(--faq-head);border-color:var(--faq-head);color:var(--white)}
.faq.open .sign{background:var(--gold)}
.faq-answer{left:99px;top:2271px;width:1002px;height:60px;border:2px solid #cfcfcf;border-top:none;padding:18px 68px;font-size:14.5px}
.more-btn{left:528px;top:2580px;width:144px;height:46px;background:var(--gold);color:var(--white);font-size:15px}

/* Contact */
.contact{left:0;top:2723px;width:1200px;height:515px;background:linear-gradient(180deg,#f2b825 0%,#e7a91a 50%,#d99a12 100%)}
.contact-title{top:2790px;color:var(--white)}
.field{background:var(--white);padding:10px 14px;font-size:13px;color:#666}
.submit{left:547px;top:3083px;width:106px;height:49px;border:2px solid var(--white);color:var(--white);font-size:16px}

/* Footer */
.footer{left:0;top:3238px;width:1200px;height:224px;background:var(--footer)}
.social{top:3215px;width:50px;height:50px;border-radius:50%;background:var(--gold);border:3px solid var(--white);display:flex;align-items:center;justify-content:center}
.foot-line{left:0;width:1200px;text-align:center;color:#d8d8d8;font-size:14px;display:flex;justify-content:center;align-items:center;gap:12px}
</style>
</head>
<body>

<!-- Hero -->
<div class="abs hero" role="img" aria-label="Rugby players in green jerseys charging forward during a match"></div>
<div class="abs hero-shade"></div>
<div class="abs brand">
  <span class="brand-mark"></span>
  <div class="brand-name">RISING CAPTAINS INITIATIVE</div>
</div>
<nav class="abs nav">
  <span class="active">HOME</span><span>PROGRAMME</span><span>BOOKING</span><span>FAQS</span><span>VANGUARDS</span><span>CONTACT US</span>
  <svg width="16" height="16" viewBox="0 0 16 16"><circle cx="6.5" cy="6.5" r="5" fill="none" stroke="#fff" stroke-width="2"/><line x1="10.3" y1="10.3" x2="15" y2="15" stroke="#fff" stroke-width="2.4"/></svg>
</nav>
<h1 class="abs hero-title">RUGBY VANGUARDS</h1>
<p class="abs hero-sub">Rugby Vanguards, a world first is the fulfilment of a desire<br>to create a colossal force for good</p>
<div class="abs btn hero-btn">BOOK NOW!</div>
<div class="abs dots"><span class="on"></span><span></span><span></span><span></span></div>

<!-- Welcome -->
<div class="abs welcome-img" role="img" aria-label="Rugby player in green carrying the ball past a tackler"></div>
<section class="abs welcome-card">
  <h2>WELCOME TO RUGBY VANGUARDS</h2>
  <p>The Rising Captains Initiative is a Rugby Vanguards initiative. This is a fantastic opportunity to lead and play the Vanguards way.</p>
  <p>The programme is open to boys and girls from the areas of 11 upwards regardless of ability or skill level. We use Rugby as the vehicle to develop your leadership, communication and teamwork.</p>
  <div class="btn small-btn">READ MORE</div>
</section>

<!-- Programs -->
<div class="abs programs"></div>
<h2 class="abs section-title" style="top:1350px">OUR PROGRAMS</h2>
<div class="abs btn tab on" style="left:339px;width:162px">BRONZE AWARD</div>
<div class="abs btn tab" style="left:517px;width:168px">SILVER AWARD</div>
<div class="abs btn tab" style="left:699px;width:162px">GOLD AWARD</div>

<div class="abs card-img" style="left:99px;background:linear-gradient(160deg,#3b5f3a,#8e3b3b 60%,#2f5a2c)" role="img" aria-label="Players contesting the ball at a ruck"></div>
<div class="abs card-img" style="left:441px;background:linear-gradient(170deg,#3a4a3a,#1a1a1a 55%,#3f6b35)" role="img" aria-label="Team in black lined up on the pitch"></div>
<div class="abs card-img" style="left:782px;background:linear-gradient(160deg,#3f6e35,#1f4a26 60%,#567a40)" role="img" aria-label="Players in green binding in a scrum"></div>

<div class="abs card-title" style="left:99px">Bronze Award (Part 1)</div>
<div class="abs card-title" style="left:441px">Bronze Award (Part 2)</div>
<div class="abs card-title" style="left:782px">Bronze Award (Part 1 &amp; Part 2)</div>

<div class="abs card-date" style="left:99px"><svg width="13" height="13" viewBox="0 0 13 13"><rect x="1" y="2" width="11" height="10" fill="none" stroke="#f7b21b" stroke-width="1.5"/><rect x="1" y="2" width="11" height="3" fill="#f7b21b"/></svg>Date 22-23 October Harrowfield</div>
<div class="abs card-date" style="left:441px"><svg width="13" height="13" viewBox="0 0 13 13"><rect x="1" y="2" width="11" height="10" fill="none" stroke="#f7b21b" stroke-width="1.5"/><rect x="1" y="2" width="11" height="3" fill="#f7b21b"/></svg>Date 20-22 Feb Kestrel Park</div>
<div class="abs card-date" style="left:782px"><svg width="13" height="13" viewBox="0 0 13 13"><rect x="1" y="2" width="11" height="10" fill="none" stroke="#f7b21b" stroke-width="1.5"/><rect x="1" y="2" width="11" height="3" fill="#f7b21b"/></svg>Date 22-23 October and 20-22 Feb</div>

<div class="abs card-price" style="left:99px">£179</div>
<div class="abs card-price" style="left:441px">£179</div>
<div class="abs card-price" style="left:782px">£300</div>

<div class="abs btn card-btn" style="left:99px">BOOK NOW!</div>
<div class="abs btn card-btn" style="left:441px">BOOK NOW!</div>
<div class="abs btn card-btn" style="left:782px">BOOK NOW!</div>

<!-- FAQs -->
<h2 class="abs section-title" style="top:2140px">FAQS</h2>
<div class="abs faq open" style="top:2229px;height:42px"><span class="sign">−</span><span class="q">Will I meet a Vanguard?</span></div>
<div class="abs faq-answer">Yes everybody that comes through the programme will meet one of the Rugby Vanguards.</div>
<div class="abs faq" style="top:2349px;height:42px"><span class="sign">+</span><span class="q">What clothes do I need to bring?</span></div>
<div class="abs faq" style="top:2414px;height:42px"><span class="sign">+</span><span class="q">Do you have a Safeguarding policy?</span></div>
<div class="abs faq" style="top:2479px;height:42px"><span class="sign">+</span><span class="q">Who attends the programme?</span></div>
<div class="abs btn more-btn">VIEW MORE</div>

<!-- Contact -->
<div class="abs contact" role="img" aria-label="Blurred rugby crowd and player washed in gold"></div>
<h2 class="abs section-title contact-title">GET IN TOUCH</h2>
<div class="abs field" style="left:258px;top:2871px;width:335px;height:42px">First Name</div>
<div class="abs field" style="left:605px;top:2871px;width:337px;height:42px">Last Name</div>
<div class="abs field" style="left:258px;top:2926px;width:335px;height:40px">Email Address</div>
<div class="abs field" style="left:605px;top:2926px;width:337px;height:40px">Phone Number</div>
<div class="abs field" style="left:258px;top:2977px;width:684px;height:83px">Message</div>
<div class="abs btn submit">SUBMIT</div>

<!-- Footer -->
<div class="abs footer"></div>
<div class="abs social" style="left:487px" aria-label="Social link"></div>
<div class="abs social" style="left:545px" aria-label="Social link"></div>
<div class="abs social" style="left:603px" aria-label="Social link"></div>
<div class="abs social" style="left:661px" aria-label="Email">
  <svg width="20" height="14" viewBox="0 0 20 14"><rect x="0" y="0" width="20" height="14" rx="1" fill="#fff"/><polyline points="1,1 10,8 19,1" fill="none" stroke="#f7b21b" stroke-width="1.6"/></svg>
</div>
<div class="abs foot-line" style="top:3309px">
  <svg width="11" height="14" viewBox="0 0 11 14"><path d="M5.5 0A5.5 5.5 0 0 0 0 5.5C0 9.5 5.5 14 5.5 14S11 9.5 11 5.5A5.5 5.5 0 0 0 5.5 0z" fill="#fff"/><circle cx="5.5" cy="5.5" r="2" fill="#0d0d0d"/></svg>
  <span>At vero eos et accusamus et iusto</span><span>|</span>
  <svg width="14" height="14" viewBox="0 0 14 14"><path d="M3 0l3 3-2 2c1 2 3 4 5 5l2-2 3 3-2 3C6 14 0 8 0 3z" fill="#fff"/></svg>
  <span>+27 80 555 0142</span><span>|</span>
  <svg width="16" height="12" viewBox="0 0 16 12"><rect width="16" height="12" rx="1" fill="#fff"/><polyline points="1,1 8,7 15,1" fill="none" stroke="#0d0d0d" stroke-width="1.4"/></svg>
  <span>info@vanguards-rci.example</span>
</div>
<div class="abs foot-line" style="top:3349px">Help &nbsp;|&nbsp; FAQ &nbsp;|&nbsp; Support &nbsp;|&nbsp; Sitemap &nbsp;|&nbsp; Terms Of Use &nbsp;|&nbsp; Privacy Statement</div>
<div class="abs foot-line" style="top:3386px">Copyrights © 2018, Rugby Vanguards. All rights reserved.</div>

</body>
</html>
```